Plovanta medical teaching of the future

responsive website, onepager, for medical technology company. It has to look clean and high tech.

Look & feel
• Responsive
• Clean
• Combination icons + foto's
• Integration of a YouTube video

Landingpage items

• Header: picture + 'a video-based teaching platform for surgical procedures'
• About Deferred live medical teaching: Short description
• Features
o Video
o Teaching platform

• Benefits:
o More effective learning
o Faster sharing of knowledge & tecniques
o More cost effective

• References

• Products:
o Live (+link to more info)
o Qorvex (+ link to more info)
o Qorvex local (+link to more info)
o Qorvex cloud (+ link to more info)

• Solutions:
o For medical device companies (+link to more info)
o Doctor and surgeons (+link to more info)
o Medical conferences (+link to more info)

Target Market(s)

medical device companies
surgeons and doctors
conference organisers

Industry/Entity Type

It Company

Number of Pages Required

1 page

Requirements
Must have
• Landingpage items
• • Header: picture + 'a video-based teaching platform for surgical procedures'
• • About Deferred live medical teaching: Short description
• • Features
• o Video
• o Teaching platform
• • Benefits:
• o More effective learning
• o Faster sharing of knowledge & tecniques
• o More cost effective
• • References
• • Products:
• o Live (+link to more info)
• o Qorvex (+ link to more info)
• o Qorvex local (+link to more info)
• o Qorvex cloud (+ link to more info)
• • Solutions:
• o For medical device companies (+link to more info)
• o Doctor and surgeons (+link to more info)
• o Medical conferences (+link to more info)
Nice to have
• possibilty to show video

```html
<!DOCTYPE html>
<html lang="en">
<head>
<meta charset="utf-8">
<title>Plovanta – Medical teaching of the future</title>
<link href="https://fonts.googleapis.com/css2?family=Open+Sans:wght@400;600;700;800&display=swap" rel="stylesheet">
<style>
:root{
  --teal:#4f8c87;
  --red:#b5121b;
  --ink:#333;
  --muted:#555;
  --light:#f2f2f2;
  --footer:#2b2b2b;
  --white:#fff;
}
*{box-sizing:border-box;margin:0;padding:0}
html,body{width:1200px;height:3905px;overflow:hidden}
body{font-family:"Open Sans",Arial,sans-serif;color:var(--ink);background:var(--white);position:relative}
section,header,footer{position:relative;width:1200px}
.abs{position:absolute}
.btn{position:absolute;display:flex;align-items:center;justify-content:center;background:var(--red);color:var(--white);font-size:14px;font-weight:700;letter-spacing:.5px;border-radius:24px;width:205px;height:44px;text-transform:uppercase}
.section-title{position:absolute;left:0;width:100%;text-align:center;color:var(--teal);font-size:28px;font-weight:700;letter-spacing:.5px;text-transform:uppercase}
.photo{position:absolute}

/* nav */
.site-header{height:94px;background:var(--white)}
.brand{position:absolute;left:75px;top:24px;display:flex;align-items:center;gap:12px;font-size:34px;font-weight:700;color:var(--teal)}
.brand-dot{width:40px;height:40px;border-radius:50%;background:var(--teal)}
.nav{position:absolute;left:398px;top:28px;display:flex;gap:0;list-style:none}
.nav li{font-size:14px;font-weight:600;color:var(--ink);padding:10px 17px;text-transform:uppercase}
.nav li.active{background:var(--red);color:var(--white);border-radius:20px}

/* hero */
.hero{height:565px;background:linear-gradient(160deg,#7fa9a5 0%,#3f6e6b 45%,#2b4b4a 100%)}
.hero h1{position:absolute;top:213px;width:100%;text-align:center;color:var(--white);font-size:40px;font-weight:800;line-height:50px;text-transform:uppercase;letter-spacing:1px}
.dots{position:absolute;top:516px;left:0;width:100%;display:flex;justify-content:center;gap:8px}
.dots span{width:10px;height:10px;background:var(--white)}
.dots span.on{background:var(--red)}

/* about */
.about{height:341px}
.about p{position:absolute;left:140px;width:920px;text-align:center;font-size:17px;line-height:32px;color:var(--muted)}

/* features */
.features{height:658px;background:var(--light)}
.feature h3{position:absolute;color:var(--red);font-size:22px;font-weight:700;text-transform:uppercase}
.feature p{position:absolute;width:500px;font-size:15px;line-height:25px;color:var(--muted)}

/* benefits */
.benefits{height:542px}
.benefits .lead{position:absolute;top:110px;left:150px;width:900px;text-align:center;font-size:17px;line-height:32px;color:var(--muted)}
.benefit{position:absolute;top:200px;width:330px;text-align:center}
.benefit .ring{width:126px;height:126px;margin:0 auto;border:2px solid #9a9a9a;border-radius:50%;display:flex;align-items:center;justify-content:center}
.benefit h3{margin-top:36px;color:var(--red);font-size:18px;font-weight:700;line-height:26px;text-transform:uppercase}
.benefit p{margin-top:8px;font-size:14px;line-height:24px;color:var(--muted)}

/* references */
.references{height:369px;background:linear-gradient(180deg,#3a3f42 0%,#24292b 100%)}
.references .section-title{color:#8fb9b5}
.references p{position:absolute;top:108px;left:110px;width:980px;text-align:center;font-size:16px;line-height:29px;color:#e8e8e8}

/* products */
.products{height:544px}
.hub{position:absolute;left:456px;top:117px;width:286px;height:286px;border-radius:50%;background:var(--white);border:10px solid #eee;box-shadow:0 0 0 1px #ddd;display:flex;align-items:center;justify-content:center;font-size:36px;font-weight:700;color:var(--teal)}
.product{position:absolute;width:270px}
.product.left{left:75px;text-align:right}
.product.right{left:867px;text-align:left}
.product h3{color:var(--red);font-size:18px;font-weight:700;text-transform:uppercase;margin-bottom:8px}
.product p{font-size:14px;line-height:23px;color:var(--muted)}
.product a,.solution a{display:block;margin-top:10px;color:var(--teal);font-size:13px;font-weight:700;text-decoration:none;text-transform:uppercase}
.pin{position:absolute;width:54px;height:54px;border-radius:50%;background:var(--white);border:1px solid #ccc;display:flex;align-items:center;justify-content:center}
.pin.filled{background:var(--red);border-color:var(--red)}

/* solutions */
.solutions{height:531px;background:var(--light)}
.solution{position:absolute;top:117px;width:331px}
.solution .photo{position:static;height:198px;width:100%}
.solution h3{margin-top:36px;color:var(--red);font-size:18px;font-weight:700;text-transform:uppercase}
.solution p{margin-top:6px;font-size:14px;line-height:22px;color:var(--muted)}

/* footer */
.site-footer{height:261px;background:var(--footer);color:#ccc}
.site-footer h4{position:absolute;top:44px;color:var(--teal);font-size:15px;font-weight:700;text-transform:uppercase;letter-spacing:.5px}
.site-footer ul{position:absolute;list-style:none;font-size:13px;line-height:31px;color:#ddd}
.social{position:absolute;left:75px;top:128px;display:flex;gap:14px}
.social span{width:16px;height:16px;border-radius:50%;background:#eee}
.copy{position:absolute;left:75px;top:187px;font-size:13px;line-height:21px;color:#ccc}
.contact{position:absolute;left:635px;top:82px;font-size:13px;line-height:21px;color:#ddd}
.contact div{display:flex;gap:10px;align-items:flex-start;margin-bottom:8px}
.field{position:absolute;left:885px;top:81px;width:241px;height:40px;border-radius:20px;background:var(--white);font-size:13px;color:#555;padding:11px 16px}
.signup{position:absolute;left:1037px;top:133px;width:90px;height:40px;border-radius:20px;background:var(--red);color:var(--white);font-size:14px;font-weight:700;display:flex;align-items:center;justify-content:center}
</style>
</head>
<body>

<header class="site-header">
  <div class="brand"><span class="brand-dot"></span>Plovanta</div>
  <ul class="nav">
    <li class="active">Home</li><li>About us</li><li>Features</li><li>Benefits</li><li>References</li><li>Products</li><li>Solutions</li>
  </ul>
</header>

<section class="hero" role="img" aria-label="Surgical team in an operating room with monitors showing a procedure">
  <h1>A video-based teaching platform<br>for surgical procedures</h1>
  <div class="btn" style="left:498px;top:340px">Read more</div>
  <div class="dots"><span class="on"></span><span></span><span></span><span></span></div>
</section>

<section class="about">
  <h2 class="section-title" style="top:44px">About deferred live medical teaching</h2>
  <p style="top:97px">Plovanta is building a video based cloud teaching platform for all kinds of medical procedures using synchronized high resolution 360° and wide angle videos in a virtual reality environment.<br>Plovanta changes the way medical procedures are taught.</p>
  <div class="btn" style="left:498px;top:238px">Read more</div>
</section>

<section class="features">
  <h2 class="section-title" style="top:44px">Features</h2>
  <div class="feature">
    <div class="photo" role="img" aria-label="Surgeons watching a procedure on large monitors" style="left:75px;top:114px;width:511px;height:255px;background:linear-gradient(150deg,#8fb3b0,#3e6b69 60%,#2d3d3f)"></div>
    <h3 style="left:75px;top:392px">Video</h3>
    <p style="left:75px;top:432px">Healthcare companies contract top surgeons to do teaching sessions with their appliances/equipment. In the case of peer-to-peer medical teachings, medical device companies fly in surgeons from all over the world to attend live surgeries.</p>
    <div class="btn" style="left:75px;top:565px">Read more</div>
  </div>
  <div class="feature">
    <div class="photo" role="img" aria-label="Operating room with surgical team and camera equipment" style="left:614px;top:114px;width:513px;height:255px;background:linear-gradient(150deg,#a8bcbc,#56797a 55%,#2f3f42)"></div>
    <h3 style="left:614px;top:392px">Teaching platform</h3>
    <p style="left:614px;top:432px">Once the surgery is captured all the info can be streamed online with the unique feature that, although the surgery is filmed in advance, the presenter has real-time full control over the imaging he wants to see.</p>
    <div class="btn" style="left:614px;top:565px">Read more</div>
  </div>
</section>

<section class="benefits">
  <h2 class="section-title" style="top:44px">Benefits</h2>
  <p class="lead">Medical and surgical knowledge can be shared in a faster, easier and more cost-effective waythan current solutions like movies and pre-edited video.</p>
  <div class="benefit" style="left:75px">
    <div class="ring"><svg width="52" height="40" viewBox="0 0 52 40" fill="none" stroke="var(--teal)" stroke-width="3"><rect x="8" y="3" width="36" height="25" rx="2"/><path d="M2 34h48l-4 4H6z"/></svg></div>
    <h3>More effective learning</h3>
    <p>of knowledge and new techniques to surgeons worldwide due to the cloud-based teaching platform..</p>
  </div>
  <div class="benefit" style="left:434px">
    <div class="ring"><svg width="54" height="40" viewBox="0 0 54 40" fill="var(--teal)"><circle cx="27" cy="10" r="7"/><circle cx="11" cy="14" r="5"/><circle cx="43" cy="14" r="5"/><path d="M15 38c0-10 5-17 12-17s12 7 12 17z"/><path d="M2 36c0-8 4-13 9-13 3 0 5 1 6 3-2 3-3 6-3 10z"/><path d="M52 36c0-8-4-13-9-13-3 0-5 1-6 3 2 3 3 6 3 10z"/></svg></div>
    <h3>Faster sharing of knowledge<br>&amp; tecniques</h3>
    <p>due to advanced video-based interactivity and state of the art medical illustrations clarifying each step of the procedure..</p>
  </div>
  <div class="benefit" style="left:793px">
    <div class="ring"><span style="font-size:56px;font-weight:700;color:var(--teal)">$</span></div>
    <h3>More cost-effective</h3>
    <p>compared to traditional teaching<br>methods</p>
  </div>
</section>

<section class="references" role="img" aria-label="Darkened operating room with surgical equipment">
  <h2 class="section-title" style="top:42px">References</h2>
  <p>Aliquam molestie, mi et imperdiet euismod, dui purus auctor tellus, et interdum lacus lectus et ante. Sed accumsan sollicitudin sapien, sit amet adipiscing turpis gravida ac. In congue, neque ac lobortis volutpat, libero mauris varius mi, vitae suscipit ipsum ligula vitae risus.</p>
  <div class="btn" style="left:498px;top:253px">Read more</div>
</section>

<section class="products">
  <h2 class="section-title" style="top:48px">Products</h2>
  <svg class="abs" style="left:0;top:0" width="1200" height="544" fill="none" stroke="#ddd" stroke-width="1.5">
    <path d="M423 159 H480 M826 159 H770 M423 367 H480 M826 367 H770"/>
  </svg>
  <div class="hub">Plovanta</div>

  <div class="product left" style="top:115px"><h3>Live</h3><p>Vestibulum ante ipsum primis in faucibus orci luctus et ultrices posuere cubilia egestas risus in magna varius nibh eget..</p><a>More info</a></div>
  <div class="pin" style="left:369px;top:132px"><svg width="26" height="20" viewBox="0 0 26 20" fill="none" stroke="var(--red)" stroke-width="2"><rect x="4" y="2" width="18" height="12"/><path d="M1 17h24"/></svg></div>

  <div class="product right" style="top:115px"><h3>Qorvex</h3><p>Vestibulum ante ipsum primis in faucibus orci luctus et ultrices posuere cubilia egestas risus in magna varius nibh eget..</p><a>More info</a></div>
  <div class="pin filled" style="left:772px;top:132px"><svg width="26" height="18" viewBox="0 0 26 18" fill="var(--white)"><rect x="1" y="3" width="16" height="12" rx="2"/><path d="M18 8l7-4v10l-7-4z"/></svg></div>

  <div class="product left" style="top:323px"><h3>Qorvex local</h3><p>Vestibulum ante ipsum primis in faucibus orci luctus et ultrices posuere cubilia egestas risus in magna varius nibh eget..</p><a>More info</a></div>
  <div class="pin" style="left:369px;top:340px"><svg width="18" height="24" viewBox="0 0 18 24" fill="var(--red)"><path d="M9 0a9 9 0 0 0-9 9c0 7 9 15 9 15s9-8 9-15a9 9 0 0 0-9-9zm0 13a4 4 0 1 1 0-8 4 4 0 0 1 0 8z"/></svg></div>

  <div class="product right" style="top:323px"><h3>Qorvex cloud</h3><p>Vestibulum ante ipsum primis in faucibus orci luctus et ultrices posuere cubilia egestas risus in magna varius nibh eget..</p><a>More info</a></div>
  <div class="pin" style="left:772px;top:340px"><svg width="28" height="18" viewBox="0 0 28 18" fill="var(--red)"><path d="M7 18a6 6 0 0 1-1-12 8 8 0 0 1 15-1 6 6 0 0 1 1 13z"/></svg></div>
</section>

<section class="solutions">
  <h2 class="section-title" style="top:48px">Solutions</h2>
  <div class="solution" style="left:75px">
    <div class="photo" role="img" aria-label="Video capture equipment cart with monitor" style="background:linear-gradient(160deg,#9aa4aa,#4a5258 60%,#1f2428)"></div>
    <h3>For medical device companies</h3>
    <p>Vestibulum ante ipsum primis in faucibus orci luctus et ultrices posuere cubilia egestas risus in magna varius nibh eget..</p><a>More info</a>
  </div>
  <div class="solution" style="left:435px">
    <div class="photo" role="img" aria-label="Surgeons operating under surgical lights" style="background:linear-gradient(160deg,#9fc1bd,#4f7f7b 55%,#2c4646)"></div>
    <h3>Doctor and surgeons</h3>
    <p>Vestibulum ante ipsum primis in faucibus orci luctus et ultrices posuere cubilia egestas risus in magna varius nibh eget..</p><a>More info</a>
  </div>
  <div class="solution" style="left:796px">
    <div class="photo" role="img" aria-label="Medical conference with a video call on a large screen" style="background:linear-gradient(160deg,#e6eef2,#b9cbd6 55%,#8aa3b3)"></div>
    <h3>Medical conferences</h3>
    <p>Vestibulum ante ipsum primis in faucibus orci luctus et ultrices posuere cubilia egestas risus in magna varius nibh eget..</p><a>More info</a>
  </div>
</section>

<footer class="site-footer">
  <div class="brand" style="top:42px;font-size:30px;color:#ddd"><span class="brand-dot" style="width:34px;height:34px;background:#ddd"></span>Plovanta</div>
  <div class="social"><span></span><span></span><span></span><span></span><span></span><span></span></div>
  <div class="copy">Copyright© 2017, Company Name<br>All Right Reserved</div>

  <h4 style="left:383px">Site map</h4>
  <ul style="left:383px;top:74px"><li>Home</li><li>About Us</li><li>Features</li><li>Benefits</li></ul>
  <ul style="left:503px;top:74px"><li>References</li><li>Products</li><li>Solutions</li></ul>

  <h4 style="left:635px">Contact us</h4>
  <div class="contact">
    <div><span>4410 Harrow Lane,<br>Leeds, LS2 7QT</span></div>
    <div><svg width="12" height="14" viewBox="0 0 12 14" fill="#ddd"><path d="M2 1l3 3-2 2c1 2 2 3 4 4l2-2 3 3-2 2C5 13 0 8 0 3z"/></svg><span>1-800-555-0142</span></div>
    <div><svg width="14" height="12" viewBox="0 0 14 12" fill="#ddd"><path d="M0 2h14v9H0zM0 2l7 5 7-5"/></svg><span>info@plovanta.example</span></div>
  </div>

  <h4 style="left:885px">Newsletter sign up</h4>
  <div class="field">Enter Email Address</div>
  <div class="signup">SIGN UP</div>
</footer>

</body>
</html>
```